PACKGING

DESIGN FOR CARTRIDGE weight (400G ) SILICONE YOU CAN SERCHE IN GOOGLE FOR SEE MODEL THE CARTRIDGE

Target Market(s)

number one 1
100% SILICONE SEALANT & ADHESIVES

Logo Text

halvendurs

Font styles to use
Sans Serif

Colors
0555a3
b768aa
33a6d7

Requirements
Nice to have
• you find drew in cartridge in web: https://www.quillmarshtradeslist.example.uk/2016/03/14/achieving-a-clean-seal-with-flexible-caulk/
• nice drew explain use product

```html
<!DOCTYPE html>
<html lang="en">
<head>
<meta charset="utf-8">
<title>KALIMOR Transparent – cartridge label</title>
<link href="https://fonts.googleapis.com/css2?family=Exo+2:ital,wght@0,700;0,800;1,600;1,700;1,800&display=swap" rel="stylesheet">
<style>
  :root{
    --stage:#b9bdc1;
    --blue:#1f3f98;
    --blue-deep:#15286f;
    --navy:#111d4b;
    --yellow:#ffdc00;
    --red:#e30613;
    --white:#ffffff;
    --text-blue:#1b3a94;
  }
  *{box-sizing:border-box;margin:0;padding:0}
  html,body{width:1200px;height:1200px;overflow:hidden}
  body{background:var(--stage);font-family:"Exo 2",sans-serif;position:relative}

  .label{
    position:absolute;left:398px;top:35px;width:404px;height:1130px;overflow:hidden;
    background:linear-gradient(180deg,var(--blue) 0%,var(--blue-deep) 55%,var(--navy) 100%);
  }
  .label > *{position:absolute}
  .decor{left:0;top:0;width:404px;height:1130px}

  .grade{left:50px;top:44px;font-size:40px;font-weight:800;font-style:italic;color:var(--white);
    transform:rotate(-3deg);transform-origin:left bottom;letter-spacing:.5px}

  .brand-box{left:50px;top:140px;width:354px;height:96px;background:var(--blue-deep)}
  .brand{left:72px;top:150px;font-size:72px;font-weight:800;color:var(--yellow);letter-spacing:1px;line-height:1}

  .variant-band{left:50px;top:232px;width:312px;height:44px;background:var(--yellow)}
  .variant{left:50px;top:236px;width:312px;text-align:center;font-size:27px;font-weight:700;font-style:italic;color:var(--text-blue)}

  .claim-box{left:59px;top:336px;width:304px;height:134px;background:linear-gradient(180deg,#2450b0,var(--blue-deep));}
  .claim{left:70px;top:350px;font-size:46px;font-weight:800;font-style:italic;color:var(--white);line-height:1}
  .claim .accent{color:#fff3a8}

  .features{left:44px;top:500px;width:350px;display:grid;grid-template-columns:1fr 1fr;row-gap:34px;column-gap:8px}
  .feature{display:flex;align-items:center;gap:8px;color:var(--white);font-size:20px;font-style:italic;font-weight:600;line-height:1.05}
  .feature svg{flex:0 0 30px}

  .photo{left:0;top:685px;width:404px;height:260px;
    background:linear-gradient(120deg,#c9ccd0 0%,#9ea4ab 45%,#e0762c 70%,#2b3c7a 100%)}

  .economy-band{left:0;top:955px;width:404px;height:95px;background:var(--red)}
  .economy{left:180px;top:985px;font-size:27px;font-weight:700;font-style:italic;color:var(--white);transform:rotate(-4deg)}
  .volume-band{left:0;top:1040px;width:404px;height:90px;background:var(--yellow)}
  .volume{left:232px;top:1052px;font-size:50px;font-weight:800;font-style:italic;color:var(--text-blue);transform:rotate(-4deg)}
  .flag{left:48px;top:1018px;width:112px;height:78px;
    background:linear-gradient(180deg,#2a3f8f 0 45%,#c8102e 45% 55%,#ffffff 55% 65%,#c8102e 65% 75%,#ffffff 75% 85%,#c8102e 85%)}
</style>
</head>
<body>
<main class="label">
  <svg class="decor" viewBox="0 0 404 1130" aria-hidden="true">
    <polygon points="0,118 404,86 404,100 0,132" fill="var(--yellow)"/>
    <rect x="40" y="125" width="5" height="200" fill="var(--yellow)"/>
    <polygon points="40,312 404,300 404,312 40,324" fill="var(--yellow)"/>
    <polyline points="59,478 363,470 363,332" fill="none" stroke="var(--yellow)" stroke-width="2"/>
    <line x1="44" y1="480" x2="44" y2="1000" stroke="var(--yellow)" stroke-width="1.5"/>
    <polygon points="0,945 404,945 404,960 0,960" fill="var(--navy)"/>
  </svg>

  <div class="grade">PROFESSIONAL</div>

  <div class="brand-box"></div>
  <div class="brand">KALIMOR</div>

  <div class="variant-band"></div>
  <div class="variant">TRANSPARENT</div>

  <div class="claim-box"></div>
  <div class="claim">100% <span class="accent">JOINT</span><br>ETANCHE</div>

  <ul class="features">
    <li class="feature">
      <svg viewBox="0 0 30 30" width="30" height="30"><circle cx="11" cy="15" r="7" fill="none" stroke="var(--yellow)" stroke-width="3"/><circle cx="19" cy="15" r="7" fill="none" stroke="var(--yellow)" stroke-width="3"/></svg>
      <span>seals &amp;<br>lubricates<br>O rings</span>
    </li>
    <li class="feature">
      <svg viewBox="0 0 30 30" width="30" height="30"><circle cx="15" cy="15" r="12" fill="none" stroke="var(--yellow)" stroke-width="2.5"/><path d="M9 18v-6M13 18v-6M17 18v-6M21 18v-6" stroke="var(--yellow)" stroke-width="2"/></svg>
      <span>fast dry<br>(rapid de<br>sèche)</span>
    </li>
    <li class="feature">
      <svg viewBox="0 0 30 30" width="30" height="30"><rect x="11" y="3" width="7" height="18" rx="3.5" fill="none" stroke="var(--yellow)" stroke-width="2.5"/><circle cx="14.5" cy="23" r="5" fill="var(--yellow)"/><path d="M21 8h4M21 12h4M21 16h4" stroke="var(--yellow)" stroke-width="2"/></svg>
      <span>temperature<br>-40 to +250</span>
    </li>
    <li class="feature">
      <svg viewBox="0 0 30 30" width="30" height="30"><rect x="4" y="11" width="11" height="8" rx="4" fill="none" stroke="var(--yellow)" stroke-width="2.5"/><rect x="15" y="11" width="11" height="8" rx="4" fill="none" stroke="var(--yellow)" stroke-width="2.5"/><path d="M15 2v5M15 23v5M5 4l3 4M25 4l-3 4" stroke="var(--yellow)" stroke-width="2"/></svg>
      <span>strong<br>(robuste)</span>
    </li>
  </ul>

  <div class="photo" role="img" aria-label="Photo of a worker in a hard hat and hi-vis vest applying sealant with a cordless caulking gun on a building site"></div>

  <div class="economy-band"></div>
  <div class="economy">ECONOMIC</div>
  <div class="volume-band"></div>
  <div class="volume">300ml</div>
  <div class="flag" role="img" aria-label="Waving United States flag"></div>
</main>
</body>
</html>
```